Bright Fern Custom Homes business card. Double sided. Modern. professional

Bright Fern Custom Homes
contemporary modern design with our logo /
Double sided with all our contact information
Use same Green colors as in our Logo. Contemporary logo that grabs your attention. Visually pleasing and balanced. Easy to read, and Vibrant. Would love an option for rounded edges. Embossed logo would be amazing.
Contact Information for Business Card
Dana Welk Owner / General Contractor Bright Fern Custom Homes p: 704.552.1830 m: 912.648.2071 e: brightferncustomhomes@mailbox.example w: www.brightferncustomhomes.example 218 Pryor Meadow Lane Larkdale, GA 30418

```html
<!DOCTYPE html>
<html lang="en">
<head>
<meta charset="utf-8">
<title>Bright Fern Custom Homes – Business Card</title>
<link href="https://fonts.googleapis.com/css2?family=Cinzel:wght@500&family=Montserrat:wght@400;500&display=swap" rel="stylesheet">
<style>
  :root {
    --fern: #6b8c2a;
    --fern-deep: #5a7a22;
    --ink: #1c1c1c;
    --card-white: #ffffff;
    --card-black: #1a1b1d;
    --backdrop: #e6e7e4;
  }
  * { margin: 0; padding: 0; box-sizing: border-box; }
  html, body { width: 1200px; height: 900px; overflow: hidden; }
  body {
    background: var(--backdrop);
    font-family: "Montserrat", sans-serif;
    color: var(--ink);
    position: relative;
  }
  .card {
    position: absolute;
    left: 320px;
    width: 560px;
    height: 320px;
    border-radius: 18px;
    overflow: hidden;
    box-shadow: 0 10px 28px rgba(0,0,0,.18);
  }
  .card--front { top: 80px; background: var(--card-white); }
  .card--back { top: 500px; background: var(--card-black); }

  .front__tab {
    position: absolute; left: 0; top: 26px;
    width: 10px; height: 34px;
    background: var(--fern);
    border-radius: 0 4px 4px 0;
  }
  .front__name {
    position: absolute; left: 36px; top: 24px;
    font-family: "Cinzel", serif; font-weight: 500;
    font-size: 30px; letter-spacing: 1px; line-height: 36px;
    color: var(--fern); text-transform: uppercase;
  }
  .front__title {
    position: absolute; left: 36px; top: 66px;
    font-size: 14px; font-weight: 500;
  }
  .front__rule {
    position: absolute; left: 0; top: 170px;
    width: 480px; height: 2px;
    background: var(--fern-deep);
  }
  .contact-list {
    position: absolute; left: 24px; top: 188px;
    list-style: none;
    font-size: 13px; font-weight: 500; line-height: 22px;
  }
  .contact-list li { display: flex; align-items: center; gap: 7px; }
  .contact-list svg { width: 12px; height: 12px; flex: none; }
  .contact-list .accent { color: var(--fern); }

  .brand {
    display: flex; align-items: center; gap: 10px;
    font-family: "Cinzel", serif; font-weight: 500;
    color: var(--fern); text-transform: uppercase;
  }
  .brand__dot { border-radius: 50%; background: var(--fern); flex: none; }
  .front__brand {
    position: absolute; right: 34px; top: 102px;
    font-size: 19px; line-height: 24px; width: 230px;
  }
  .front__brand .brand__dot { width: 22px; height: 22px; }

  .front__address {
    position: absolute; right: 34px; top: 212px;
    text-align: right; font-style: normal;
    font-size: 14px; font-weight: 500; line-height: 22px;
  }

  .back__brand {
    position: absolute; left: 50%; top: 50%;
    transform: translate(-50%, -50%);
    font-size: 32px; line-height: 40px;
    white-space: nowrap;
  }
  .back__brand .brand__dot { width: 34px; height: 34px; }
</style>
</head>
<body>
  <section class="card card--front" aria-label="Card front">
    <div class="front__tab"></div>
    <h1 class="front__name">Dana Welk</h1>
    <p class="front__title">Owner / General Contractor</p>
    <div class="front__rule"></div>

    <ul class="contact-list">
      <li>
        <svg viewBox="0 0 12 12" aria-hidden="true"><path d="M2.5 1l2 2.2-1 1.3c.7 1.4 1.6 2.3 3 3l1.3-1 2.2 2-1.3 1.5C5 10 2 7 1 2.3z" fill="var(--fern)"/></svg>
        704.552.1830
      </li>
      <li>
        <svg viewBox="0 0 12 12" aria-hidden="true"><rect x="3" y="1" width="6" height="10" rx="1.2" fill="none" stroke="var(--fern)" stroke-width="1.4"/></svg>
        912.648.2071
      </li>
      <li>
        <svg viewBox="0 0 12 12" aria-hidden="true"><rect x="1" y="2.5" width="10" height="7" fill="none" stroke="var(--fern)" stroke-width="1.3"/><path d="M1 2.5l5 4 5-4" fill="none" stroke="var(--fern)" stroke-width="1.3"/></svg>
        brightferncustomhomes@mailbox.example
      </li>
      <li>
        <svg viewBox="0 0 12 12" aria-hidden="true"><circle cx="6" cy="6" r="5" fill="none" stroke="var(--fern)" stroke-width="1.2"/><path d="M1 6h10M6 1c-2.5 3-2.5 7 0 10M6 1c2.5 3 2.5 7 0 10" fill="none" stroke="var(--fern)" stroke-width="1"/></svg>
        <span>www.<span class="accent">brightferncustomhomes.example</span></span>
      </li>
    </ul>

    <div class="brand front__brand">
      <span class="brand__dot"></span>
      <span>Bright Fern Custom Homes</span>
    </div>

    <address class="front__address">
      218 Pryor Meadow<br>Lane Larkdale,<br>GA 30418
    </address>
  </section>

  <section class="card card--back" aria-label="Card back">
    <div class="brand back__brand">
      <span class="brand__dot"></span>
      <span>Bright Fern<br>Custom Homes</span>
    </div>
  </section>
</body>
</html>
```